Innovative Industrial Technology Start up need complete branding solution!

Corvana88 are a specialist industrial Technology solution provider offering End to End Control Systems, Electrical, Industrial IT and Communications services to the Energy, Resources and Infrastructure sectors.

Our ethos is to nurture and deliver creative, innovative and sustainable industrial technology solutions through the use of latest technologies and cutting edge industry practices. Our approach is progressive and personal, balancing wider project economics between return on investment and process metrics to promote value and positive returns to our clients.

We are looking for a contemporary, fresh, edgy and captivating brand. Simple and effective as well as scale-able. The brand should reflect our progressive approach to project delivery while representing a youthful yet professional image. Bold Colours, strong fonts along with clean lines for any logos.

We are looking for the following deliverables:
1) Corporate brand and style guide
2) Business Cards
3) Letterhead
4) Formatted word document (including cover page\table of contents\tables\appendix)
5) Email Signature
6) Capability Statement (Outline only - Text can be provided)

A Sample document is provided from a similar organisation for information.

Target Market(s)

Energy, Resources, Infrastructure

Industry/Entity Type

Progressive

Logo Text

Corvana88

Logo styles of interest
Abstract Logo
Wordmark Logo
Lettermark Logo
Font styles to use
Serif
Sans Serif

```html
<!DOCTYPE html>
<html lang="en">
<head>
<meta charset="utf-8">
<title>Corvana88 Letterhead</title>
<link rel="stylesheet" href="https://fonts.googleapis.com/css2?family=Quicksand:wght@400;500;700&display=swap">
<style>
  :root {
    --brand-red: #7a1418;
    --ink: #1c1c1c;
    --text: #2a2a2a;
    --mono-grey: #e4e4e4;
    --paper: #ffffff;
  }
  html, body {
    margin: 0;
    padding: 0;
    overflow: hidden;
    background: var(--paper);
  }
  .letterhead {
    position: relative;
    width: 934px;
    height: 1200px;
    background: var(--paper);
    overflow: hidden;
    font-family: "Quicksand", sans-serif;
    color: var(--text);
  }
  .frame {
    position: absolute;
    inset: 0;
    width: 934px;
    height: 1200px;
  }
  .sender {
    position: absolute;
    left: 600px;
    top: 132px;
  }
  .sender__name {
    margin: 0 0 16px;
    font-weight: 700;
    font-size: 16px;
    letter-spacing: 1.6px;
    color: var(--ink);
  }
  .sender__details {
    margin: 0;
    padding: 0;
    list-style: none;
    font-size: 13.5px;
    font-weight: 500;
    line-height: 20.5px;
    letter-spacing: 1.1px;
  }
  .monogram {
    position: absolute;
    left: 257px;
    top: 383px;
    width: 406px;
    height: 392px;
    border-radius: 48% 52% 45% 55% / 40% 40% 60% 60%;
    background: radial-gradient(ellipse at center, var(--mono-grey) 0%, #f3f3f3 60%, var(--paper) 100%);
  }
  .brand-block {
    position: absolute;
    left: 192px;
    top: 946px;
    width: 535px;
    text-align: center;
  }
  .brand-block__dot {
    display: block;
    width: 106px;
    height: 106px;
    margin: 0 auto;
    border-radius: 50%;
    background: var(--brand-red);
  }
  .brand-block__name {
    margin: 20px 0 0;
    font-size: 20px;
    font-weight: 400;
    letter-spacing: 26px;
    padding-left: 26px;
    color: var(--text);
    line-height: 24px;
  }
  .brand-block__rule {
    height: 0;
    border: 0;
    border-top: 1.5px solid var(--ink);
    margin: 13px 0 0;
  }
  .brand-block__tagline {
    margin: 10px 0 0;
    font-size: 19.5px;
    font-weight: 500;
    letter-spacing: 1px;
    color: var(--ink);
  }
</style>
</head>
<body>
  <main class="letterhead">
    <svg class="frame" viewBox="0 0 934 1200" aria-hidden="true">
      <g fill="none" stroke="var(--brand-red)" stroke-width="1.5">
        <polyline points="875,53 875,118 599,118"/>
        <polyline points="599,266 875,266 875,1125"/>
      </g>
    </svg>

    <header class="sender">
      <h1 class="sender__name">CORVANA88</h1>
      <ul class="sender__details">
        <li>Address</li>
        <li>Email</li>
        <li>Telephone</li>
        <li>www.corvana88.com</li>
      </ul>
    </header>

    <div class="monogram" role="img" aria-label="Large faint script monogram of the brand initials"></div>

    <footer class="brand-block">
      <span class="brand-block__dot" aria-hidden="true"></span>
      <p class="brand-block__name">CORVANA88</p>
      <hr class="brand-block__rule">
      <p class="brand-block__tagline">sustainable industrial technology solutions</p>
    </footer>
  </main>
</body>
</html>
```